Letterhead for a German Distribution/Manufacturing Company

We need a professional Letterhead in a unique Design.
not to playful.
The Letterhead has to show show that we are a international company with headquater in Germany.
all details like adress, Vat Tax Number, Bank Accout, Eori, email, Company number has to be on the Letterhead.
for example use: VAT TAX DE5704168 Bank Account: Norrfeld Bank IBAN DE421705238ß310482 Swift: KOLV3154802 EORI 3041296587 Company Number: HRB 61508 Adress: VOLTRINA UG Amsel Strasse 7 Postal Code 04683 City Halvenstadt Country: Germany Email: info@voltrina-example.com
the design can be colored but doesnt have to be
Industry/Entity Type
Manufacturing and international distribution
Requirements
Must have
- show that we are a international company with headquater in Germany. our company infos and logo

```html
<!DOCTYPE html>
<html lang="en">
<head>
<meta charset="utf-8">
<title>VOLTRINA Letterhead</title>
<link rel="stylesheet" href="https://fonts.googleapis.com/css2?family=Montserrat:wght@400;500&family=Open+Sans:wght@400;700&family=Great+Vibes&display=swap">
<style>
  :root {
    --backdrop: #b6b7bb;
    --paper: #ffffff;
    --brand-dark: #4a4a4a;
    --brand-tab-light: #5a5a5a;
    --text-body: #2b2b2b;
    --text-muted: #a3a3a3;
    --footer-band: #4d4d4d;
  }
  * { margin: 0; padding: 0; box-sizing: border-box; }
  html, body {
    width: 1123px; height: 1200px; overflow: hidden;
    background: var(--backdrop);
  }
  .letterhead {
    position: absolute; left: 146px; top: 12px;
    width: 830px; height: 1176px;
    background: var(--paper);
    font-family: "Open Sans", Arial, sans-serif;
    color: var(--text-body);
  }
  .brand-tab {
    position: absolute; left: 83px; top: 0;
    width: 105px; height: 168px;
    background: linear-gradient(90deg, var(--brand-dark), var(--brand-tab-light));
    border-radius: 0 0 9px 9px;
  }
  .brand-name {
    position: absolute; left: 199px; top: 80px;
    font-family: "Montserrat", Arial, sans-serif;
    font-weight: 500; font-size: 46px; letter-spacing: 1px;
    color: var(--brand-dark); line-height: 1;
  }
  .recipient { position: absolute; left: 87px; top: 296px; }
  .recipient-name { font-size: 15px; color: var(--text-muted); line-height: 20px; }
  .recipient-role { font-size: 11.5px; color: var(--text-body); line-height: 18px; }
  .letter-body {
    position: absolute; left: 87px; top: 380px; width: 700px;
    font-size: 13.9px; line-height: 28px; color: var(--text-body);
    white-space: nowrap;
  }
  .letter-body p + p { margin-top: 28px; }
  .sign-off { position: absolute; left: 87px; top: 850px; }
  .signature {
    font-family: "Great Vibes", cursive;
    font-size: 32px; line-height: 38px; color: #1e1e1e;
  }
  .signer-name { font-weight: 700; font-size: 13.6px; line-height: 17px; color: #1e1e1e; }
  .signer-role { font-size: 13.6px; line-height: 17px; color: var(--text-body); }
  .company-details {
    position: absolute; left: 82px; top: 1054px; list-style: none;
    font-family: "Montserrat", Arial, sans-serif;
    font-weight: 500; font-size: 11.6px; color: #333;
    white-space: nowrap;
  }
  .company-details li {
    display: flex; align-items: center; height: 21px;
  }
  .detail-icon { width: 15px; height: 15px; margin-right: 13px; flex: none; }
  .footer-band {
    position: absolute; left: 0; bottom: 0; width: 100%; height: 24px;
    background: var(--footer-band);
  }
</style>
</head>
<body>
<main class="letterhead">
  <div class="brand-tab"></div>
  <div class="brand-name">VOLTRINA</div>

  <section class="recipient">
    <div class="recipient-name">Jonas Dorn</div>
    <div class="recipient-role">Chief Director</div>
  </section>

  <section class="letter-body">
    <p>This is a sample letter that has been placed to demonstrate typing remat (Your Company). letterhead<br>design. When positioned properly, it will serve to work in harmony with all other elements letterhead.<br>This letterhead design is meant to project an image</p>
    <p>This letterhead design is meant project an image of professionalism reliability. By using simple aligen<br>we have created a very spacious feeling. The simplicity suggest&nbsp; rengththe spaciousnes contributes h<br>aesthetics the layout. These basic qualities along with the (Your Company)</p>
    <p>look and helps reinforce the (Your Company) brand. letterhead design is meant to project an image p<br>design. When positioned properly, it will serve to work in harmony all the other elements letterhead.<br>sionalism and reliability.</p>
    <p>This letterhead design is based on the (Form of your logo) form (Your Company) logo. Each stationery<br>we have created a very spacious feeling. The simplicity suggests strength the spaciousnes contribute<br>part of the (Form of your logo).</p>
  </section>

  <section class="sign-off">
    <div class="signature">Lukas Brenner</div>
    <div class="signer-name">Lukas Brenner</div>
    <div class="signer-role">Manager</div>
  </section>

  <ul class="company-details">
    <li>
      <svg class="detail-icon" viewBox="0 0 16 16"><circle cx="8" cy="8" r="7.5" fill="#4a4a4a"/></svg>
      VAT TAX DE5704168 Bank Account: Norrfeld Bank IBAN DE421705238ß310482
    </li>
    <li>
      <svg class="detail-icon" viewBox="0 0 16 16"><circle cx="8" cy="8" r="7.5" fill="#4a4a4a"/></svg>
      Swift: KOLV3154802 EORI 3041296587 Company Number: HRB 61508
    </li>
    <li>
      <svg class="detail-icon" viewBox="0 0 16 16">
        <circle cx="8" cy="8" r="7.5" fill="#4a4a4a"/>
        <path d="M8 3.5a3 3 0 0 0-3 3c0 2.2 3 5.8 3 5.8s3-3.6 3-5.8a3 3 0 0 0-3-3z" fill="#fff"/>
        <circle cx="8" cy="6.5" r="1.1" fill="#4a4a4a"/>
      </svg>
      Adress: VOLTRINA UG Amsel Strasse 7 Postal Code 04683 City Halvenstadt Germany.
    </li>
    <li>
      <svg class="detail-icon" viewBox="0 0 16 16">
        <circle cx="8" cy="8" r="7.5" fill="#4a4a4a"/>
        <circle cx="8" cy="8" r="4.5" fill="none" stroke="#fff" stroke-width="1.2"/>
        <path d="M3.5 8h9M8 3.5c-2 2.5-2 6.5 0 9M8 3.5c2 2.5 2 6.5 0 9" fill="none" stroke="#fff" stroke-width="1"/>
      </svg>
      Email: info@voltrina-example.com
    </li>
  </ul>

  <div class="footer-band"></div>
</main>
</body>
</html>
```